Book Cover (QUIET WEEKS MEND EVERY KNOT)

This book is a series of blog posts from my blog, Sparks Kept Handy, which is at glenferrante.example/blog.
The book is to be called:
QUIET WEEKS MEND EVERY KNOT
And 51 other Sparks Kept Handy from the Corner Shop Tutor
(Sparks Kept Handy) should be italicized.
My name is Glen Ferrante, M.B.A.

I will need three variations for my paperback, hardcover and e-book.
Here are some of the blog titles and their topics:
Preparing Your Small Business For Recession small business recession
Should I Incorporate My Business? Should I Incorporate My Business?
Alternative to Minority Shareholder In Small Private Companies minority shareholder
Small Business Culture – Getting it Right Small Business Culture
What is The Right Way to Fire Someone The Right Way to Fire Someone
The Five Basic Leadership Principles Leadership Principles
10 Tips for New Entrepreneurs – Sure Ways to Increase Your Chances of Success
10 things to consider before becoming an entrepreneur
Strategy vs Biz Plans small business strategy
Closing Sales close the sale
Breakeven break even
Growth makes cash flow suck cash flow issues
Think Twice About Offering Early Payment Discounts prepayment discounts
Firing Customers firing customers
Collections best practices getting paid faster
The Cash Flow Statement cash flow statement
Using Paralegals paralegal
Radical Candor radical candor
Why No is the Second Best Word to a Salesperson's ears value of no
The $8 Million Problem -
Contractor vs Employee contractor vs employee
The Columbo sales tactic
Systems Turn Goals From Dreams Into Reality Systems vs Goals
The Importance of Realistic Goals stretch goals
Why The Owner Must Review Every Hire hiring for values
Systems Thinking for Small Biz: The Case for SOPs systems thinking
Trust Your Gut business intuition
Grease and friction grease vs friction
Left alone, 90% of problems solve themselves strategic inaction
Referrals Are Great—But Not a Growth Strategy referrals
The Lean Marketing Machine: 7 Hacks to Grow Your Small Business Fast marketing hacks
The Small Business Health Check small business health check
How to Spot a Customer Headed for Trouble — Before They Take You Down With Them customer warning signs
We Are What We Repeatedly Do habits
The Smartest People Know When to Play Dumb playing dumb
Before You Scale, Do the Math unit economics
AI for Small Business: Practical Tools and Use Cases AI for Small Business
Title: Tell Me Right Now—Why Can’t We Raise Your Prices? small business pricing
Why Your Real Competitor Isn’t Who You Think creative destruction
Good Enough Might Be Great satisficing
Bootstrapping: Building Your Business on Your Terms bootstrapping
Building Resilient Companies That Never Have to Bet the Farm bet the farm
We Always Overshoot: From Fiber to Cannabis to AI AI overbuild
A Bias Toward Action bias toward ation
Choosing the Right Business Owner Title business owner title
Jobs to Be Done: Understanding What Your Customers Really Want Jobs to Be Done
Forget Money. Here’s What Really Motivates People. motivation

Target Market(s)

Small business operators, business school students

Industry/Entity Type

Small business

Colors

Designer to choose colors to be used in the design.

Requirements
Should not have
• Should not look cartoonish

```html
<!DOCTYPE html>
<html lang="en">
<head>
<meta charset="utf-8">
<title>Quiet Weeks Mend Every Knot — Book Cover</title>
<link rel="stylesheet" href="https://fonts.googleapis.com/css2?family=Nunito+Sans:wght@700&family=Lato:ital,wght@0,400;1,400&family=Roboto+Condensed:wght@700&display=swap">
<style>
  :root {
    --cover-paper: #eae8e3;
    --ink: #1b1b1b;
    --accent-green: #52b83a;
    --note-light: #f4dfae;
    --note-mid: #e7c47f;
    --note-edge: #d4a860;
    --note-ink: #2a2418;
    --band: #151515;
  }
  * { margin: 0; padding: 0; box-sizing: border-box; }
  html, body { width: 800px; height: 1200px; overflow: hidden; background: var(--cover-paper); }
  .book-cover {
    position: relative;
    width: 800px;
    height: 1200px;
    background: var(--cover-paper);
    overflow: hidden;
  }
  .title-block { position: absolute; left: 0; top: 0; width: 800px; height: 680px; }
  .title-line {
    font-family: "Nunito Sans", "Avenir Next", sans-serif;
    font-weight: 700;
    fill: var(--ink);
  }
  .title-line--accent { fill: var(--accent-green); }
  .subtitle-note {
    position: absolute;
    left: 190px;
    top: 708px;
    width: 410px;
    height: 210px;
    padding: 30px 34px;
    transform: rotate(-8deg);
    background: radial-gradient(ellipse at 50% 45%, var(--note-light) 0%, var(--note-mid) 70%, var(--note-edge) 100%);
    box-shadow: 6px 10px 14px rgba(0,0,0,0.28);
    display: flex;
    align-items: center;
    justify-content: center;
    text-align: center;
    font-family: "Lato", sans-serif;
    font-size: 28px;
    line-height: 1.2;
    color: var(--note-ink);
  }
  .series-name { font-style: italic; }
  .author-band {
    position: absolute;
    left: 0;
    bottom: 0;
    width: 800px;
    height: 80px;
    background: var(--band);
    display: flex;
    align-items: center;
    justify-content: center;
    font-family: "Roboto Condensed", sans-serif;
    font-weight: 700;
    font-size: 42px;
    color: var(--accent-green);
  }
</style>
</head>
<body>
  <main class="book-cover">
    <svg class="title-block" viewBox="0 0 800 680" xmlns="http://www.w3.org/2000/svg" aria-label="Quiet Weeks Mend Every Knot">
      <text class="title-line" x="74" y="238" font-size="205" textLength="664" lengthAdjust="spacingAndGlyphs">QUIET</text>
      <text class="title-line" x="74" y="376" font-size="112" textLength="654" lengthAdjust="spacingAndGlyphs">WEEKS</text>
      <text class="title-line title-line--accent" x="76" y="542" font-size="196" textLength="648" lengthAdjust="spacingAndGlyphs">MEND</text>
      <text class="title-line" x="78" y="640" font-size="90" textLength="644" lengthAdjust="spacingAndGlyphs">EVERY KNOT</text>
    </svg>

    <div class="subtitle-note">
      <p>And 51 other Sparks Kept Handy from the Corner Shop Tutor <span class="series-name">(Sparks Kept Handy)</span></p>
    </div>

    <footer class="author-band">Glen Ferrante, M.B.A</footer>
  </main>
</body>
</html>
```